Company Letter head for formal business correspondence

Company needs a new facelift for stationary. Our letter head is impact as a professional service provider. We need to reflect professionalism in the Safety and Health environment. we work in the whole of the asia pacific region with our main base in Australia Queensland. We are a service company with consulting and operational focus. I have supplied our current logo. I have attached also our first letterhead that we didn't use, Wrong address on it also as we have moved since

Reason: Extension for design review due to modification with some designs currently and Xmas break issue.

Target Market(s)

New clients, government and global companys

Industry/Entity Type

Business

Font styles to use
Sans Serif

Requirements
Must have
• Logo, address, be in word format so l can use as a template and not just printed paper that l place in a printer.
• 41 Corlett Rd, Rockhampton, Queensland 4812.
• 1300718246 info@velminor.com
Nice to have
• a water mark in the back ground of the logo or partial log as one example supplied

```html
<!DOCTYPE html>
<html lang="en">
<head>
<meta charset="utf-8">
<title>Velminor Letterhead</title>
<link href="https://fonts.googleapis.com/css2?family=Open+Sans:wght@400;600;700&display=swap" rel="stylesheet">
<style>
  :root {
    --backdrop: #c0c0c0;
    --paper: #ffffff;
    --ink: #1c1c1c;
    --brand-red: #c21f26;
    --brand-red-dark: #981d22;
    --rule: #b8262c;
    --watermark-grey: #eaeaea;
    --watermark-red: #f6e3e4;
    --signature-tone: #f1f1f1;
  }
  * { margin: 0; padding: 0; box-sizing: border-box; }
  html, body {
    width: 1200px; height: 1200px; overflow: hidden;
    background: var(--backdrop);
    font-family: "Open Sans", sans-serif;
    color: var(--ink);
  }
  .letterhead {
    position: absolute; left: 209px; top: 47px;
    width: 781px; height: 1105px;
    background: var(--paper); overflow: hidden;
  }
  .watermark { position: absolute; left: 0; top: 0; pointer-events: none; }
  .brand {
    position: absolute; left: 77px; top: 62px;
    display: flex; align-items: center; gap: 12px;
  }
  .brand-dot { width: 30px; height: 30px; border-radius: 50%; background: var(--brand-red); }
  .brand-name { font-size: 42px; font-weight: 700; letter-spacing: 1px; color: var(--ink); line-height: 1; }
  .contact {
    position: absolute; left: 557px; top: 46px; height: 80px;
    border-left: 1.5px solid var(--rule); padding-left: 13px;
    font-size: 10.5px; line-height: 16px;
  }
  .contact-row { display: flex; align-items: center; gap: 5px; }
  .contact-row svg { width: 11px; height: 11px; fill: var(--brand-red); }
  .contact-address { margin-top: 3px; line-height: 12px; }
  .letter-body {
    position: absolute; left: 77px; top: 204px; width: 640px;
    font-size: 13.2px; line-height: 27.6px;
  }
  .letter-title { font-weight: 700; margin-bottom: 27px; }
  .letter-body p { margin-bottom: 27.6px; }
  .sign-off { margin-top: 0; }
  .signature {
    width: 200px; height: 66px; margin: 2px 0 16px;
    background: var(--signature-tone); border-radius: 4px;
  }
  .footer-band { position: absolute; left: 0; bottom: 0; width: 781px; height: 39px; }
</style>
</head>
<body>
  <main class="letterhead">
    <svg class="watermark" width="781" height="1105" viewBox="0 0 781 1105" aria-hidden="true">
      <circle cx="580" cy="880" r="176" fill="var(--watermark-grey)"/>
      <circle cx="590" cy="880" r="120" fill="var(--watermark-red)"/>
    </svg>

    <header class="brand">
      <span class="brand-dot"></span>
      <span class="brand-name">VELMINOR</span>
    </header>

    <address class="contact" style="font-style:normal">
      <div class="contact-row">
        <svg viewBox="0 0 24 24"><path d="M6.6 10.8a15 15 0 0 0 6.6 6.6l2.2-2.2a1 1 0 0 1 1-.25 11.4 11.4 0 0 0 3.6.57 1 1 0 0 1 1 1V20a1 1 0 0 1-1 1A17 17 0 0 1 3 4a1 1 0 0 1 1-1h3.5a1 1 0 0 1 1 1c0 1.25.2 2.45.57 3.57a1 1 0 0 1-.25 1z"/></svg>
        <span>1300718246</span>
      </div>
      <div class="contact-row">
        <svg viewBox="0 0 24 24"><path d="M2 5h20v14H2zm2 2v.5l8 5 8-5V7zm0 2.8V17h16V9.8l-8 5z"/></svg>
        <span>info@velminor.com</span>
      </div>
      <div class="contact-row">
        <svg viewBox="0 0 24 24"><path d="M12 2a10 10 0 1 0 0 20 10 10 0 0 0 0-20zm6.9 9h-3a15 15 0 0 0-1.3-5.6A8 8 0 0 1 18.9 11zM12 4.1c.9 1.2 1.8 3.6 1.9 6.9h-3.8c.1-3.3 1-5.7 1.9-6.9zM9.4 5.4A15 15 0 0 0 8.1 11h-3a8 8 0 0 1 4.3-5.6zM5.1 13h3a15 15 0 0 0 1.3 5.6A8 8 0 0 1 5.1 13zm6.9 6.9c-.9-1.2-1.8-3.6-1.9-6.9h3.8c-.1 3.3-1 5.7-1.9 6.9zm2.6-1.3a15 15 0 0 0 1.3-5.6h3a8 8 0 0 1-4.3 5.6z"/></svg>
        <span>www.velminor.com</span>
      </div>
      <div class="contact-address">41 Corlett Rd, Rockhampton<br>Queensland 4812</div>
    </address>

    <section class="letter-body">
      <h1 class="letter-title" style="font-size:13.2px">Lorem Ipsum is simply</h1>
      <p>&nbsp;dummy text of the printing and typesetting industry. Lorem Ipsum has been the industry's standard dummy text ever since the 1500s, when an unknown printer took a galley of type and scrambled it to make a type specimen book. It has survived not only five centuries, but also the leap into electronic typesetting, remaining essentially unchanged.</p>
      <p>It is a long established fact that a reader will be distracted by the readable content of a page when looking at its layout. The point of using Lorem Ipsum is that it has a more-or-less normal distribution of letters, as opposed to using 'Content here, content here', making it look like readable English. Many desktop publishing packages and web page editors now use Lorem Ipsum as their default model text, and a search for 'lorem ipsum' will uncover many web sites still in their infancy. Various versions have evolved over the years, sometimes by accident, sometimes on purpose (injected humour and the like).</p>
      <p>&nbsp;Contrary to popular belief, Lorem Ipsum is not simply random text. It has roots in a piece of classical Latin literature from 45 BC, making it over 2000 years old. Henry Dalworth, a Latin professor at Ashford Hill College in Virginia, looked up one of the more obscure Latin words, consectetur, from a Lorem Ipsum passage,</p>
      <div class="sign-off">Lorem Ipsum</div>
      <div class="signature" role="img" aria-label="Handwritten signature"></div>
      <div class="sign-off">Lorem Ipsum is a dummy</div>
    </section>

    <svg class="footer-band" viewBox="0 0 781 39" aria-hidden="true">
      <rect width="781" height="39" fill="var(--brand-red)"/>
      <polygon points="570,0 672,0 660,39 558,39" fill="var(--brand-red-dark)"/>
      <polygon points="684,0 781,0 781,39 672,39" fill="var(--brand-red-dark)"/>
    </svg>
  </main>
</body>
</html>
```